Redesign an App Mockup for Messaging app

I want one page redesigned for my app & 1 icon built from scratch.

I also want a few simple color changes on 5 of the other pages.

i can help you get the changes right, you can message me on Skype: Torvim82

first person finished wins the contest

```html
<!DOCTYPE html>
<html lang="en">
<head>
<meta charset="utf-8">
<title>Hollo Chat – Inbox</title>
<link rel="stylesheet" href="https://fonts.googleapis.com/css2?family=Roboto:wght@300;400;500&family=Open+Sans:wght@400&display=swap">
<style>
:root{
  --brand:#29bed6;
  --brand-dark:#22aac0;
  --white:#ffffff;
  --ink:#3a3a3a;
  --ink-soft:#6e6e6e;
  --divider:#e3e3e3;
  --badge-bg:#ececec;
  --dot-blue:#29bed6;
  --dot-black:#2b2b2b;
  --dot-yellow:#f5c018;
  --art-tone:#e9f6f9;
  --art-tone-2:#d5eef3;
  --ghost-tone:#f1f1f1;
}
*{margin:0;padding:0;box-sizing:border-box}
html,body{width:676px;height:1200px;overflow:hidden;background:var(--white)}
.screen{position:relative;width:676px;height:1200px;overflow:hidden;background:var(--white);font-family:"Roboto",Arial,sans-serif;color:var(--ink)}

.topbar{position:absolute;left:0;top:0;width:676px;height:122px;background:var(--brand);color:var(--white)}
.status{position:absolute;top:0;left:0;width:100%;height:36px;font-size:24px;font-weight:400}
.status .carrier{position:absolute;left:16px;top:4px;display:flex;align-items:center;gap:4px}
.status .time{position:absolute;left:0;right:0;top:4px;text-align:center;font-weight:500}
.status .battery{position:absolute;right:14px;top:4px;display:flex;align-items:center;gap:8px}
.app-title{position:absolute;left:0;right:0;top:46px;text-align:center;font-size:64px;font-weight:400;letter-spacing:0.5px;line-height:72px}
.action{position:absolute;top:48px}
.action.add-friend{left:20px}
.action.compose{right:22px}

.threads{position:absolute;left:0;top:122px;width:676px;list-style:none}
.thread{position:relative;height:118px;border-bottom:1px solid var(--divider)}
.thread .dot{position:absolute;left:32px;top:40px;width:39px;height:39px;border-radius:50%;display:flex;align-items:center;justify-content:center;gap:3px}
.thread .dot i{width:5px;height:5px;border-radius:50%;background:var(--white);display:block}
.dot.blue{background:var(--dot-blue)}
.dot.black{background:var(--dot-black)}
.dot.yellow{background:var(--dot-yellow)}
.thread .name{position:absolute;left:101px;top:36px;font-size:35px;font-weight:400;color:var(--ink);line-height:44px}
.thread.has-meta .name{top:22px}
.thread .meta{position:absolute;left:102px;top:70px;font-family:"Open Sans",Arial,sans-serif;font-size:22px;color:var(--ink-soft)}
.thread .state{position:absolute;right:32px;top:42px;width:35px;height:35px;border-radius:50%;background:var(--badge-bg);display:flex;align-items:center;justify-content:center}
.thread .count{position:absolute;right:30px;top:44px;font-family:"Open Sans",Arial,sans-serif;font-size:23px;color:var(--ink-soft)}

.art-goal{position:absolute;left:424px;top:906px;width:222px;height:134px;border-radius:10px;background:linear-gradient(160deg,var(--art-tone),var(--art-tone-2))}
.art-ghost{position:absolute;left:56px;top:1018px;width:86px;height:86px;border-radius:40px 40px 14px 14px;background:var(--ghost-tone)}
</style>
</head>
<body>
<main class="screen">
  <header class="topbar">
    <div class="status">
      <span class="carrier">
        <svg width="76" height="14" viewBox="0 0 76 14"><g fill="#fff"><circle cx="7" cy="7" r="6"/><circle cx="22" cy="7" r="6"/><circle cx="37" cy="7" r="6"/></g><g fill="none" stroke="#fff" stroke-width="1.4"><circle cx="52" cy="7" r="5.3"/><circle cx="67" cy="7" r="5.3"/></g></svg>
        Operator
        <svg width="24" height="18" viewBox="0 0 24 18"><path d="M12 17 2 6a14 14 0 0 1 20 0z" fill="#fff"/></svg>
      </span>
      <span class="time">11:27 AM</span>
      <span class="battery">100 %
        <svg width="50" height="22" viewBox="0 0 50 22"><rect x="1" y="1" width="44" height="20" rx="3" fill="none" stroke="#fff" stroke-width="1.6"/><rect x="4" y="4" width="38" height="14" rx="1.5" fill="#fff"/><rect x="46" y="7" width="3" height="8" rx="1" fill="#fff"/></svg>
      </span>
    </div>
    <h1 class="app-title">Hollo Chat</h1>
    <svg class="action add-friend" width="66" height="66" viewBox="0 0 66 66" aria-label="Add friend">
      <circle cx="26" cy="18" r="13" fill="#fff"/>
      <path d="M2 56c0-14 10-24 24-24s24 10 24 24z" fill="#fff"/>
      <circle cx="47" cy="47" r="15" fill="#fff" stroke="var(--brand)" stroke-width="3"/>
      <path d="M47 39v16M39 47h16" stroke="var(--brand)" stroke-width="4" stroke-linecap="round"/>
    </svg>
    <svg class="action compose" width="60" height="60" viewBox="0 0 60 60" aria-label="New message">
      <rect x="4" y="8" width="48" height="48" rx="8" fill="none" stroke="#fff" stroke-width="5"/>
      <path d="M20 42l3-11 24-24 8 8-24 24z" fill="var(--brand)" stroke="#fff" stroke-width="4" stroke-linejoin="round"/>
      <path d="M41 13l8 8" stroke="#fff" stroke-width="4"/>
    </svg>
  </header>

  <ul class="threads">
    <li class="thread">
      <span class="dot blue"><i></i><i></i><i></i></span>
      <span class="name">rivenloop</span>
      <span class="state"><svg width="20" height="16" viewBox="0 0 20 16"><path d="M8 1 1 7l7 6V9c5 0 8 1 11 6-1-6-4-10-11-10z" fill="var(--brand)"/></svg></span>
    </li>
    <li class="thread has-meta">
      <span class="dot black"><i></i><i></i><i></i></span>
      <span class="name">tq2290</span>
      <span class="meta">Sunday - Double tap to reply</span>
      <span class="state"><svg width="20" height="16" viewBox="0 0 20 16"><path d="M8 1 1 7l7 6V9c5 0 8 1 11 6-1-6-4-10-11-10z" fill="var(--brand)"/></svg></span>
    </li>
    <li class="thread has-meta">
      <span class="dot yellow"><i></i><i></i><i></i></span>
      <span class="name">m_oakly</span>
      <span class="meta">Friday - Opened</span>
      <span class="count">15</span>
    </li>
    <li class="thread">
      <span class="dot blue"><i></i><i></i><i></i></span>
      <span class="name">lumi_waffless</span>
      <span class="state"><svg width="20" height="16" viewBox="0 0 20 16"><path d="M8 1 1 7l7 6V9c5 0 8 1 11 6-1-6-4-10-11-10z" fill="var(--brand)"/></svg></span>
    </li>
    <li class="thread">
      <span class="dot black"><i></i><i></i><i></i></span>
      <span class="name">orvalin</span>
      <span class="state"><svg width="20" height="16" viewBox="0 0 20 16"><path d="M8 1 1 7l7 6V9c5 0 8 1 11 6-1-6-4-10-11-10z" fill="var(--brand)"/></svg></span>
    </li>
    <li class="thread">
      <span class="dot yellow"><i></i><i></i><i></i></span>
      <span class="name">kdelmarrow7</span>
      <span class="state"><svg width="18" height="14" viewBox="0 0 18 14"><path d="M2 7l5 5L16 2" fill="none" stroke="var(--dot-yellow)" stroke-width="2.6" stroke-linecap="round" stroke-linejoin="round"/></svg></span>
    </li>
  </ul>

  <div class="art-goal" role="img" aria-label="Illustration of a mascot standing in a soccer goal"></div>
  <div class="art-ghost" role="img" aria-label="Faint mascot illustration"></div>
</main>
</body>
</html>
```